2021 IT Training Presentation Deck Refresh

Copper Lantern is an IT education services firm. We teach IT industry standards and technologies. We are in need of an updated training presentation deck that factors in a fresh take for:

1) Agenda/Table of Contents
2) Chapter Topic Summary
2) Chapter Introduction and Learning Objectives
3) Chapter Recaps
4) Important Point/Pro Tip emphasis
5) Warning Message
6) Mini Quiz layout
7) Lab Exercise Introduction
7) Deck Close Out

Incorporating the official Copper Lantern colour palette for materials that will likely be used in self-paced/online recorded versions of courses.

Target Market(s)

IT

Industry/Entity Type

Computer Training

Requirements
Nice to have
• placeholder sections for images of IT workers in an office or by a computer

```html
<!DOCTYPE html>
<html lang="en">
<head>
<meta charset="utf-8">
<title>Copper Lantern – Training Deck Overview</title>
<link href="https://fonts.googleapis.com/css2?family=Montserrat:wght@300;400;600;700;800&display=swap" rel="stylesheet">
<style>
:root{
  --blue:#0b9de6;
  --ink:#1c1c1c;
  --body:#3a3a3a;
  --muted:#b9b9b9;
  --rule:#222222;
  --panel:#ebebeb;
  --soft:#efeff0;
  --placeholder:#d6d6d6;
}
*{box-sizing:border-box;margin:0;padding:0}
html,body{width:1200px;height:675px;overflow:hidden;background:#fff}
.canvas{position:relative;width:1200px;height:675px;overflow:hidden;font-family:"Montserrat",sans-serif;color:var(--ink)}
.board-left{position:absolute;left:0;top:0;width:429px;height:675px;background:#fff}
.board-right{position:absolute;left:429px;top:0;width:771px;height:675px;background:var(--panel)}
.caption{position:absolute;left:0;top:592px;width:429px;text-align:center;font-weight:800;font-size:18.5px;line-height:22.5px;color:#111}
.heading{position:absolute;left:462px;top:42px;width:260px;text-align:center;font-weight:800;font-size:21px;line-height:23px;color:#111}

.slide{position:absolute;background:#fff;overflow:hidden;font-family:"Montserrat",sans-serif}
.slide.sm{width:188px;height:105px;font-size:10px}
.slide.lg{width:226px;height:127px;font-size:12px;box-shadow:0 2px 6px rgba(0,0,0,.08)}
.slide.soft{background:var(--soft)}
.logo{position:absolute;left:5%;top:5.5%;display:flex;align-items:center;gap:.5em;font-size:.3em;font-weight:600;color:var(--blue);letter-spacing:.02em;z-index:5;text-transform:uppercase}
.logo::before{content:"";width:1.6em;height:1.6em;border-radius:50%;background:var(--blue)}
.logo.light{color:#fff}.logo.light::before{background:#fff}
.title{position:absolute;font-weight:400;font-size:1em;line-height:1.12;text-transform:uppercase;letter-spacing:.05em;color:var(--ink);z-index:3}
.title.r{text-align:right}
.rule{position:absolute;height:1px;background:var(--rule);z-index:3}
.text{position:absolute;font-size:.33em;line-height:1.5;color:var(--body);z-index:3}
.text.dim{color:var(--muted)}
.pg{position:absolute;right:6%;bottom:6%;width:1.9em;height:1.9em;font-size:.22em;border:1px solid #555;border-radius:50%;display:grid;place-items:center;color:#444}
.corner-tr{position:absolute;right:0;top:0;width:14%;height:28%;z-index:4}
.corner-tr::before{content:"";position:absolute;right:0;top:0;width:100%;height:32%;background:var(--blue)}
.corner-tr::after{content:"";position:absolute;right:0;top:0;width:42%;height:100%;background:var(--blue);border-bottom-left-radius:35%}
.corner-tr.white::before,.corner-tr.white::after{background:#fff}
.corner-bl{position:absolute;left:0;bottom:0;width:14%;height:28%;z-index:4}
.corner-bl::before{content:"";position:absolute;left:0;bottom:0;width:100%;height:32%;background:var(--blue)}
.corner-bl::after{content:"";position:absolute;left:0;bottom:0;width:48%;height:100%;background:var(--blue)}
.photo{position:absolute;z-index:2}
.photo.navy{background:linear-gradient(135deg,#0b1836,#1e3663 55%,#12244a)}
.photo.desk{background:linear-gradient(135deg,#c9b69a,#e6e0d6 55%,#9fb1c4)}
.photo.office{background:linear-gradient(135deg,#4d6f7c,#8ea7b0)}
.photo.wood{background:linear-gradient(135deg,#b88d5c,#dcc5a1 60%,#c5cdd6)}
.photo.coffee{background:linear-gradient(135deg,#4a2f1e,#7b5436 45%,#3a2418)}
.photo.cotton{background:linear-gradient(90deg,rgba(239,239,240,0),#dcd9d4 40%,#c9c3bb)}
.photo.warn{background:linear-gradient(135deg,#d8c7a6,#e5c43c 45%,#d9c9a8)}
.photo.solar{background:linear-gradient(135deg,#22355a,#7e95b3)}
.bordered{border-top:.18em solid var(--blue);border-bottom:.18em solid var(--blue)}
.dot{position:absolute;aspect-ratio:1;border-radius:50%;background:var(--blue);color:#fff;display:grid;place-items:center;text-align:center;font-weight:400;z-index:3}
.dot.grey{background:#dcdcdc;color:#9a9a9a}
.time{width:10%;font-size:.34em;line-height:1.05}
.letter{width:9.5%;font-size:.5em}
.vline{position:absolute;width:1px;background:var(--blue);z-index:2}
.toc-row{position:absolute;left:30%;right:20%;font-size:.34em;display:flex;align-items:baseline;gap:.4em;color:var(--body)}
.toc-row span.lead{flex:1;border-bottom:1px dotted #888}
</style>
</head>
<body>
<div class="canvas">

  <section class="board-left">

    <article class="slide sm" style="left:22px;top:22px">
      <div class="logo">Copper Lantern</div>
      <div style="position:absolute;left:79%;top:0;width:21%;height:79%;background:var(--blue);border-bottom-left-radius:100% 45%;z-index:1"></div>
      <h1 class="title r" style="right:7%;top:16%;font-size:1.25em">Training Title</h1>
      <div class="text" style="right:7%;top:30%;font-size:.26em;letter-spacing:.1em">DATE</div>
      <div class="rule" style="left:7.5%;right:0;top:38%"></div>
      <div class="photo navy" style="left:7.5%;top:43%;width:85%;bottom:0" role="img" aria-label="Photo placeholder: network of connected people icons on a dark tech background"></div>
      <div style="position:absolute;left:0;top:83%;width:21%;bottom:0;background:var(--blue);border-top-right-radius:100% 100%;z-index:4"></div>
    </article>

    <article class="slide sm" style="left:221px;top:22px">
      <div class="logo">Copper Lantern</div>
      <h2 class="title r" style="right:36%;top:25%">Welcome</h2>
      <div class="rule" style="left:0;width:64%;top:39%"></div>
      <div class="photo" style="left:16.5%;top:42%;width:15%;aspect-ratio:1;border-radius:50%;background:linear-gradient(160deg,#c4c4c4,#8d8d8d)" role="img" aria-label="Portrait placeholder for the facilitator"></div>
      <div class="text" style="left:38%;top:47%">Some introduction from the facilitator.</div>
      <div class="text" style="left:10%;width:27%;top:72%;text-align:center;font-size:.24em;letter-spacing:.15em">DANA ELLIS</div>
      <div class="text" style="left:10%;width:27%;top:79%;text-align:center">Speaker</div>
      <div class="pg">2</div>
    </article>

    <article class="slide sm" style="left:22px;top:137px">
      <div class="logo">Copper Lantern</div>
      <div class="corner-tr"></div>
      <h2 class="title r" style="right:39%;top:13%">Agenda with<br>timing</h2>
      <div class="rule" style="left:0;width:61%;top:38%"></div>
      <div class="dot time" style="left:15%;top:41%">3:00<br>PM</div>
      <div class="text" style="left:27%;top:42%;width:22%">Lorem ipsum dolor sit amet, consectetur adipiscing elit.</div>
      <div class="dot time" style="left:53.5%;top:41%">5:00<br>PM</div>
      <div class="text" style="left:65%;top:42%;width:23%">Vestibulum ante ipsum primis in faucibus orci luctus.</div>
      <div class="dot time" style="left:15%;top:63%">3:00<br>PM</div>
      <div class="text" style="left:27%;top:66%;width:23%">Etiam lacinia fermentum est non lobortis.</div>
      <div class="dot time" style="left:53.5%;top:63%">5:00<br>PM</div>
      <div class="text" style="left:65%;top:66%;width:23%">Lorem ipsum available, but the majority have.</div>
      <div class="pg">4</div>
    </article>

    <article class="slide sm soft" style="left:221px;top:137px">
      <div class="logo">Copper Lantern</div>
      <div class="photo cotton" style="left:62%;top:0;right:0;bottom:0" role="img" aria-label="Photo placeholder: cotton branch on a light background"></div>
      <div class="corner-tr"></div>
      <h2 class="title" style="left:6%;top:27%">First chapter<br>title example</h2>
      <div class="rule" style="left:0;width:48%;top:50%"></div>
      <div class="text" style="left:6%;top:54%">First part quick summary text.</div>
      <div class="pg">6</div>
    </article>

    <article class="slide sm" style="left:22px;top:250px">
      <div class="logo">Copper Lantern</div>
      <h2 class="title r" style="right:59%;top:19%">Mini quiz<br>rules</h2>
      <div class="rule" style="left:0;width:41%;top:43%"></div>
      <div class="text" style="left:6%;top:46%;width:36%">Etiam sit amet cursus nulla. Nunc quis iaculis odio. Curabitur id faucibus neque. Sed ante tortor, tempor eget lectus sed, suscipit scelerisque metus. Vestibulum faucibus neque nunc, vitae ornare turpis hendrerit quis.</div>
      <div class="dot" style="left:69%;top:14%;width:21%">
        <svg viewBox="0 0 40 40" width="38%" fill="none" stroke="#1b3a5c" stroke-width="1.6"><circle cx="20" cy="15" r="8"/><circle cx="20" cy="15" r="5"/><path d="M15 21 l-3 12 5-3 3 4 M25 21 l3 12 -5-3 -3 4"/></svg>
      </div>
      <div class="text" style="left:69%;width:21%;top:44%;text-align:center;color:#fff;font-size:.2em;letter-spacing:.15em;z-index:4">WHAT'S TO WIN</div>
      <div class="dot" style="left:48%;top:45%;width:21%">
        <svg viewBox="0 0 40 40" width="38%" fill="none" stroke="#1b3a5c" stroke-width="1.6"><circle cx="20" cy="20" r="11"/><path d="M20 13 v7 l5 3"/></svg>
      </div>
      <div class="text" style="left:48%;width:21%;top:76%;text-align:center;color:#fff;font-size:.2em;letter-spacing:.15em;z-index:4">WHAT'S THE<br>TIME</div>
      <div class="pg">7</div>
    </article>

    <article class="slide sm" style="left:221px;top:250px">
      <div class="logo">Copper Lantern</div>
      <h2 class="title" style="left:7%;top:29%;font-size:.95em">Mini quiz</h2>
      <div class="rule" style="left:0;width:38%;top:41%"></div>
      <div class="text" style="left:7%;top:44%;width:34%">First question of the multiple choice mini quiz</div>
      <div class="corner-bl"></div>
      <div class="vline" style="left:55%;top:12%;bottom:12%"></div>
      <div class="dot letter" style="left:50.5%;top:15%">A</div>
      <div class="text" style="left:62%;top:17%;width:32%">First Option. Lorem ipsum dolor sit amet, consectetur adipiscing elit. Proin aliquet eget mauris a mollis.</div>
      <div class="dot letter" style="left:50.5%;top:39%">B</div>
      <div class="text" style="left:62%;top:41%;width:32%">Second Option. Maecenas ornare sed tortor ut eleifend. Sed porttitor diam sed varius rhoncus.</div>
      <div class="dot letter" style="left:50.5%;top:63%">C</div>
      <div class="text" style="left:62%;top:65%;width:32%">Third Option. Praesent cursus tincidunt nisl ac placerat. Quisque nec neque porta, commodo risus vitae.</div>
      <div class="pg">8</div>
    </article>

    <article class="slide sm" style="left:22px;top:364px">
      <div class="photo coffee" style="inset:0;z-index:1" role="img" aria-label="Photo placeholder: hands toasting with coffee cups"></div>
      <div class="logo light">Copper Lantern</div>
      <div class="corner-tr white"></div>
      <h2 class="title" style="left:41%;top:33%;color:#fff;font-size:.95em">Coffee break</h2>
      <div class="rule" style="left:41%;right:0;top:45%;background:#fff"></div>
    </article>

    <article class="slide sm" style="left:221px;top:364px">
      <div class="logo">Copper Lantern</div>
      <div class="photo wood bordered" style="left:0;top:26%;width:41%;height:55%" role="img" aria-label="Photo placeholder: hand placing a block on a wooden tower"></div>
      <div style="position:absolute;left:0;top:71%;width:15%;aspect-ratio:1;border-radius:0 0 100% 0;background:var(--blue);z-index:3"></div>
      <div class="vline" style="left:55%;top:0;bottom:0;background:#ccc"></div>
      <div class="dot letter grey" style="left:50.5%;top:13%">A</div>
      <div class="text dim" style="left:62%;top:15%;width:32%">Lorem ipsum dolor sit amet, consectetur adipiscing elit. Proin aliquet eget mauris a mollis.</div>
      <div class="dot letter" style="left:50.5%;top:37%">B</div>
      <div class="text" style="left:62%;top:39%;width:32%">Correct answer! Maecenas ornare sed tortor ut eleifend. Sed porttitor diam sed varius rhoncus.</div>
      <div class="dot letter grey" style="left:50.5%;top:61%">C</div>
      <div class="text dim" style="left:62%;top:63%;width:32%">Praesent cursus tincidunt nisl ac placerat. Quisque nec neque porta, commodo risus vitae.</div>
      <div class="pg">10</div>
    </article>

    <article class="slide sm" style="left:22px;top:478px">
      <div class="logo">Copper Lantern</div>
      <div class="corner-tr"></div>
      <div class="photo desk bordered" style="left:6%;top:24%;width:27%;height:29%" role="img" aria-label="Photo placeholder: person working at a laptop"></div>
      <div class="photo office bordered" style="left:34.5%;top:24%;width:27%;height:29%" role="img" aria-label="Photo placeholder: hand writing on a chalkboard"></div>
      <div class="photo wood bordered" style="left:6%;top:57%;width:27%;height:29%" role="img" aria-label="Photo placeholder: wooden block tower"></div>
      <div class="photo wood bordered" style="left:34.5%;top:57%;width:27%;height:29%" role="img" aria-label="Photo placeholder: stacked blocks on a desk"></div>
      <div class="text" style="left:65.5%;top:31%;width:26%">Donec luctus diam vel velit pellentesque, sit amet commodo enim tincidunt. Ut et ornare mauris. Etiam venenatis, nibh id sollicitudin gravida, neque elit sodales quam, et vehicula dolor.</div>
      <div class="pg">21</div>
    </article>

    <article class="slide sm" style="left:221px;top:478px">
      <div class="logo">Copper Lantern</div>
      <h2 class="title r" style="right:33%;top:24%">Thank you</h2>
      <div class="rule" style="left:0;width:67%;top:38%"></div>
      <div class="text" style="left:10%;width:29%;top:43%;text-align:right;font-weight:700;color:var(--ink)">Visit us at:<br>For more info call:<br>Visit our website:</div>
      <div class="text" style="left:41%;top:43%">address<br>555 0142 386<br>www.copperlantern.example</div>
      <div class="corner-bl"></div>
      <div class="pg">22</div>
    </article>

    <p class="caption">Fully customizable slide deck<br>All grey zones are for pictures upload<br>20+ different set up included</p>
  </section>

  <section class="board-right">
    <p class="heading" style="left:33px">All pictures are for illustration purpose only</p>
  </section>

  <article class="slide lg" style="left:460px;top:170px">
    <div class="logo">Copper Lantern</div>
    <h2 class="title" style="left:30%;top:15%">Table of contents</h2>
    <div class="rule" style="left:0;width:80%;top:28%"></div>
    <div class="toc-row" style="top:34%">Introduction<span class="lead"></span>01</div>
    <div class="toc-row" style="top:45%">First Part<span class="lead"></span>02</div>
    <div class="toc-row" style="top:56%">Second Part<span class="lead"></span>03</div>
    <div class="toc-row" style="top:67%">Summary<span class="lead"></span>04</div>
    <div class="toc-row" style="top:78%">Contacts<span class="lead"></span>05</div>
    <div class="pg">3</div>
  </article>

  <article class="slide lg" style="left:702px;top:170px">
    <div class="logo">Copper Lantern</div>
    <div class="photo desk bordered" style="left:60%;top:18%;right:0;height:50%" role="img" aria-label="Photo placeholder: hand building a block tower"></div>
    <h2 class="title" style="left:6%;top:28%;font-size:.9em">Learning<br>objectives</h2>
    <div class="rule" style="left:0;width:56%;top:50%"></div>
    <div class="text" style="left:6%;top:54%;width:48%">Etiam sit amet cursus nulla. Nunc quis iaculis odio. Curabitur id faucibus neque. Sed ante tortor, tempor eget lectus sed, suscipit metus.</div>
    <div class="pg">5</div>
  </article>

  <article class="slide lg" style="left:944px;top:170px">
    <div class="logo">Copper Lantern</div>
    <div class="corner-tr"></div>
    <div class="photo desk bordered" style="left:0;top:30%;width:40%;height:48%" role="img" aria-label="Photo placeholder: team reviewing documents at a laptop"></div>
    <h2 class="title" style="left:46%;top:14%;font-size:.9em">Chapter<br>summary</h2>
    <div class="rule" style="left:44%;right:0;top:36%"></div>
    <div class="text" style="left:46%;top:40%;width:44%">Lorem ipsum dolor sit amet, consectetur adipiscing elit. Phasellus eros velit, imperdiet eget scelerisque id, maximus in nunc. Sed lacinia tortor non metus finibus fermentum.</div>
    <div class="pg">12</div>
  </article>

  <article class="slide lg" style="left:460px;top:313px">
    <div class="logo">Copper Lantern</div>
    <div class="corner-tr"></div>
    <h2 class="title r" style="right:14%;top:29%">Important point</h2>
    <div class="rule" style="left:0;right:10%;top:42%"></div>
    <div class="text" style="right:14%;top:46%;width:60%;text-align:right">Sed venenatis turpis quis quam aliquet imperdiet. In maximus, magna et laoreet maximus, erat erat fringilla sem, nec rhoncus dolor eros id nunc.</div>
    <div class="pg">13</div>
  </article>

  <article class="slide lg" style="left:702px;top:313px">
    <div class="logo">Copper Lantern</div>
    <h2 class="title r" style="right:52%;top:33%;font-size:.9em">Another<br>important point</h2>
    <div class="rule" style="left:0;width:50%;top:60%"></div>
    <div class="text" style="left:52%;top:30%;width:40%">Lorem ipsum dolor sit amet, consectetur adipiscing elit. Proin aliquet eget mauris a mollis. Aenean vel viverra quam.<br><br>Phasellus ullamcorper augue et metus auctor maximus. Donec imperdiet, ex ut tincidunt congue, elit diam feugiat tellus.</div>
    <div class="pg">14</div>
  </article>

  <article class="slide lg" style="left:944px;top:313px">
    <div class="logo">Copper Lantern</div>
    <div class="photo warn bordered" style="left:18%;top:16%;right:6%;height:36%" role="img" aria-label="Photo placeholder: yellow caution wet floor sign"></div>
    <h2 class="title r" style="right:6%;top:57%;font-size:.9em">Warning message</h2>
    <div class="rule" style="left:0;right:4%;top:68%"></div>
    <div class="text" style="left:14%;right:6%;top:72%">Pellentesque habitant morbi tristique senectus et netus et malesuada fames ac turpis egestas. Ut maximus felis ac eros ultricies.</div>
    <div class="pg">19</div>
  </article>

  <article class="slide lg" style="left:460px;top:456px">
    <div class="logo">Copper Lantern</div>
    <div class="corner-tr"></div>
    <div class="photo navy bordered" style="left:6%;top:28%;width:26%;height:30%" role="img" aria-label="Photo placeholder: network icons on a dark background"></div>
    <div class="photo solar bordered" style="left:33%;top:20%;width:28%;height:66%" role="img" aria-label="Photo placeholder: solar panels under a clear sky"></div>
    <div class="photo desk bordered" style="left:6%;top:61%;width:26%;height:25%" role="img" aria-label="Photo placeholder: hands typing on a laptop"></div>
    <div class="text" style="left:66%;top:26%;width:26%">Curabitur id tellus nec sem pellentesque fermentum et eget orci. Sed tincidunt bibendum mi, in ullamcorper quam tempor nec. Donec in finibus dui.</div>
    <div class="pg">20</div>
  </article>

  <article class="slide lg" style="left:702px;top:456px">
    <div class="logo">Copper Lantern</div>
    <div style="position:absolute;left:79%;top:0;width:21%;height:79%;background:var(--blue);border-bottom-left-radius:100% 45%;z-index:1"></div>
    <h2 class="title r" style="right:7%;top:16%;font-size:1.25em">Training Title</h2>
    <div class="text" style="right:7%;top:30%;font-size:.26em;letter-spacing:.1em">DATE</div>
    <div class="rule" style="left:7.5%;right:0;top:38%"></div>
    <div class="photo navy" style="left:7.5%;top:43%;width:85%;bottom:0" role="img" aria-label="Photo placeholder: network of connected people icons on a dark tech background"></div>
    <div style="position:absolute;left:0;top:83%;width:21%;bottom:0;background:var(--blue);border-top-right-radius:100% 100%;z-index:4"></div>
  </article>

  <article class="slide lg" style="left:944px;top:456px">
    <div class="logo">Copper Lantern</div>
    <h2 class="title" style="left:7%;top:29%;font-size:.95em">Mini quiz</h2>
    <div class="rule" style="left:0;width:38%;top:41%"></div>
    <div class="text" style="left:7%;top:44%;width:34%">First question of the multiple choice mini quiz</div>
    <div class="corner-bl"></div>
    <div class="vline" style="left:55%;top:12%;bottom:12%"></div>
    <div class="dot letter" style="left:50.5%;top:15%">A</div>
    <div class="text" style="left:62%;top:17%;width:32%">First Option. Lorem ipsum dolor sit amet, consectetur adipiscing elit.</div>
    <div class="dot letter" style="left:50.5%;top:39%">B</div>
    <div class="text" style="left:62%;top:41%;width:32%">Second Option. Maecenas ornare sed tortor ut eleifend.</div>
    <div class="dot letter" style="left:50.5%;top:63%">C</div>
    <div class="text" style="left:62%;top:65%;width:32%">Third Option. Praesent cursus tincidunt nisl ac placerat.</div>
    <div class="pg">9</div>
  </article>

</div>
</body>
</html>
```